indépendant en tant que Massothérapeute et Préparateur Mental, j'ai besoin de ...

Massothérapeute et préparateur mental indépendant, je recherche une carte de visite sobre et dynamique, sans images liées au massage ou à la préparation mentale mais intégrant mon logo. Les couleurs que j'aime bien sont : Blanc, gris, anthracite, noir et jaune

Contact Information for Business Card

carte de préférence Horizontale
neutre qui puisse toucher le deux domaines Massothérapie et préparation mentale

Requirements
Must have
• mon projet doit intégrer au recto:
LOGO
Loïc Vermande
078 315 26 49
info@loicvermande-exemple.ch
et éventuellement www.loicvermande-exemple.ch

et au verso les deux adresses:

Chemin des Ormelets 27B
1400 Yverdon-les-Bains

Rue des Tanneries 9
1700 Fribourg

Should not have
• mon projet ne doit pas contenir d'image en liens avec le massage ni la préparation mentale.

```html
<!DOCTYPE html>
<html lang="fr">
<head>
<meta charset="utf-8">
<title>Loïc Vermande – Cartes de visite</title>
<link rel="stylesheet" href="https://fonts.googleapis.com/css2?family=Montserrat:wght@400;500;600;700&display=swap">
<style>
  :root {
    --page-bg: #e4e5e7;
    --front-light: #fbfbfb;
    --front-mid: #e9eaeb;
    --back-light: #c9c9c9;
    --back-mid: #a9a9a9;
    --anthracite: #3a3a3a;
    --ink: #111111;
    --text-grey: #555555;
  }
  * { box-sizing: border-box; margin: 0; padding: 0; }
  html, body { width: 1200px; height: 913px; overflow: hidden; }
  body {
    background: var(--page-bg);
    font-family: "Montserrat", sans-serif;
    position: relative;
  }
  .card {
    position: absolute;
    width: 540px;
    height: 340px;
    border-radius: 18px;
    box-shadow: 0 10px 24px rgba(0,0,0,0.18);
    overflow: hidden;
  }
  .card-front {
    left: 60px; top: 90px;
    background: linear-gradient(120deg, var(--front-mid) 0%, var(--front-light) 45%, var(--front-mid) 100%);
  }
  .card-back {
    left: 600px; top: 470px;
    background: linear-gradient(120deg, var(--back-mid) 0%, var(--back-light) 50%, var(--back-mid) 100%);
  }
  .brand {
    position: absolute;
    display: flex;
    align-items: center;
    gap: 12px;
  }
  .brand-mark { width: 16px; height: 16px; flex: none; }
  .brand-name { font-weight: 600; letter-spacing: 0.02em; line-height: 1; white-space: nowrap; }
  .brand-tagline {
    font-size: 9.5px; font-weight: 500; letter-spacing: 0.08em;
    text-transform: uppercase; margin-top: 4px; white-space: nowrap;
  }
  .card-front .brand { left: 150px; top: 52px; color: var(--anthracite); }
  .card-front .brand-mark { background: var(--anthracite); }
  .card-front .brand-name { font-size: 26px; }
  .card-front .brand-tagline { color: var(--text-grey); }
  .holder { position: absolute; left: 40px; top: 180px; color: var(--anthracite); }
  .holder-name { font-size: 21px; font-weight: 700; letter-spacing: 0.04em; }
  .holder-role { font-size: 12px; color: var(--text-grey); margin-top: 4px; }
  .contact-list { list-style: none; margin-top: 16px; }
  .contact-list li {
    display: flex; align-items: center; gap: 10px;
    font-size: 15px; color: var(--anthracite); margin-bottom: 6px;
  }
  .contact-list svg { width: 14px; height: 14px; flex: none; }
  .card-back .brand { left: 46px; top: 100px; color: var(--ink); }
  .card-back .brand-mark { background: var(--ink); }
  .card-back .brand-name { font-size: 28px; font-weight: 700; }
  .card-back .brand-tagline { color: var(--anthracite); }
  .addresses {
    position: absolute; left: 310px; top: 170px; width: 200px;
    font-size: 13px; color: var(--anthracite); line-height: 1.45;
    font-style: normal;
  }
  .address-divider { border: none; border-top: 1.5px solid var(--anthracite); margin: 6px 0; width: 150px; }
</style>
</head>
<body>
  <section class="card card-front" aria-label="Recto">
    <div class="brand">
      <span class="brand-mark"></span>
      <div>
        <div class="brand-name">Loïc Vermande</div>
        <div class="brand-tagline">Massothérapeute / Préparateur Mental</div>
      </div>
    </div>
    <div class="holder">
      <div class="holder-name">LOÏC VERMANDE</div>
      <div class="holder-role">Director</div>
      <ul class="contact-list">
        <li>
          <svg viewBox="0 0 16 16"><path d="M4 1.5l2.5 3-1.5 1.8a9 9 0 0 0 4.7 4.7l1.8-1.5 3 2.5-1.6 2.2C7.5 14.5 1.5 8.5 1.8 3.1z" fill="var(--anthracite)"/></svg>
          <span>078 315 26 49</span>
        </li>
        <li>
          <svg viewBox="0 0 16 16"><rect x="1" y="3" width="14" height="10" rx="1" fill="var(--anthracite)"/><path d="M1.5 3.8L8 9l6.5-5.2" fill="none" stroke="#fff" stroke-width="1.2"/></svg>
          <span>info@loicvermande-exemple.ch</span>
        </li>
        <li>
          <svg viewBox="0 0 16 16"><circle cx="8" cy="8" r="7" fill="var(--anthracite)"/><path d="M1 8h14M8 1c-3 3.5-3 10.5 0 14M8 1c3 3.5 3 10.5 0 14" fill="none" stroke="#fff" stroke-width="0.9"/></svg>
          <span>www.loicvermande-exemple.ch</span>
        </li>
      </ul>
    </div>
  </section>

  <section class="card card-back" aria-label="Verso">
    <div class="brand">
      <span class="brand-mark"></span>
      <div>
        <div class="brand-name">Loïc Vermande</div>
        <div class="brand-tagline">Massothérapeute / Préparateur Mental</div>
      </div>
    </div>
    <address class="addresses">
      <div>Rue des Tanneries 9</div>
      <div>1700 Freiburg</div>
      <hr class="address-divider">
      <div>Chemin des Ormelets 27B</div>
      <div>1400 Yverdon-les-Bains</div>
    </address>
  </section>
</body>
</html>
```